Business Cards

Need a neat design for a new business card

Industry/Entity Type

Residential Construction

Contact Information for Business Card

Company Name- KOVE Construction Inc.
Owner- Marcus Tolliver
Phone number- (555)203-7481
Email- kovecohomes@brindlemail.example
Facebook- www.socialpage.example/kovecohomes

Colors
fefdec

```html
<!DOCTYPE html>
<html lang="en">
<head>
<meta charset="utf-8">
<title>KOVE Construction Inc. — Business Card</title>
<link rel="stylesheet" href="https://fonts.googleapis.com/css2?family=Roboto:wght@400;700&display=swap">
<style>
  :root {
    --backdrop: #2b2e33;
    --card: #ffffff;
    --ink: #111111;
    --muted: #9a9a9a;
    --rule: #b5b5b5;
    --icon-bg: #111111;
    --icon-fg: #ffffff;
  }
  * { box-sizing: border-box; margin: 0; padding: 0; }
  html, body {
    width: 1200px; height: 900px; overflow: hidden;
    background: var(--backdrop);
    font-family: "Roboto", Arial, sans-serif;
  }
  .sheet {
    width: 1200px; height: 900px;
    display: flex; align-items: center; justify-content: center; gap: 40px;
  }
  .card {
    position: relative;
    width: 540px; height: 310px;
    background: var(--card);
    border-radius: 30px;
  }
  .brand {
    display: flex; flex-direction: column; align-items: center;
    color: var(--ink); font-weight: 700; line-height: 1;
  }
  .brand-name { letter-spacing: 0.06em; }
  .brand-sub { letter-spacing: 0.24em; margin-top: 8px; }
  .card-front { display: flex; align-items: center; justify-content: center; }
  .card-front .brand-name { font-size: 60px; }
  .card-front .brand-sub { font-size: 16px; }

  .card-back .brand { position: absolute; top: 40px; right: 50px; }
  .card-back .brand-name { font-size: 36px; }
  .card-back .brand-sub { font-size: 10px; margin-top: 6px; }
  .rule {
    position: absolute; left: 40px; right: 40px; top: 150px;
    height: 1px; background: var(--rule);
  }
  .contact { position: absolute; left: 40px; top: 172px; }
  .owner-name { font-size: 15px; font-weight: 700; color: var(--ink); letter-spacing: 0.02em; }
  .owner-role { font-size: 10px; color: var(--muted); margin: 2px 0 10px; }
  .contact-list { list-style: none; }
  .contact-item {
    display: flex; align-items: center; gap: 9px;
    font-size: 12px; color: var(--ink); height: 20px;
  }
  .contact-icon {
    width: 14px; height: 14px; background: var(--icon-bg);
    display: flex; align-items: center; justify-content: center; flex: none;
  }
  .contact-icon svg { width: 10px; height: 10px; }
</style>
</head>
<body>
<main class="sheet">
  <section class="card card-front" aria-label="Card front">
    <div class="brand">
      <span class="brand-name">KOVE</span>
      <span class="brand-sub">CONSTRUCTION</span>
    </div>
  </section>

  <section class="card card-back" aria-label="Card back">
    <div class="brand">
      <span class="brand-name">KOVE</span>
      <span class="brand-sub">CONSTRUCTION</span>
    </div>
    <div class="rule"></div>
    <div class="contact">
      <p class="owner-name">MARCUS TOLLIVER</p>
      <p class="owner-role">Owner</p>
      <ul class="contact-list">
        <li class="contact-item">
          <span class="contact-icon">
            <svg viewBox="0 0 10 10" aria-hidden="true"><path d="M2 1 L4 1 L4.6 3 L3.5 3.8 Q4.3 5.7 6.2 6.5 L7 5.4 L9 6 L9 8 Q8.5 9 7.5 9 Q1 8.5 1 2.5 Q1 1.5 2 1 Z" fill="var(--icon-fg)"/></svg>
          </span>
          (555)203-7481
        </li>
        <li class="contact-item">
          <span class="contact-icon">
            <svg viewBox="0 0 10 10" aria-hidden="true"><rect x="1" y="2.2" width="8" height="5.6" fill="none" stroke="var(--icon-fg)" stroke-width="1"/><path d="M1 2.4 L5 5.4 L9 2.4" fill="none" stroke="var(--icon-fg)" stroke-width="1"/></svg>
          </span>
          kovecohomes@brindlemail.example
        </li>
        <li class="contact-item">
          <span class="contact-icon"></span>
          www.socialpage.example/kovecohomes
        </li>
      </ul>
    </div>
  </section>
</main>
</body>
</html>
```